Expo Program Guide Design and Logo for Lantern Grove Shows

First, we are looking for a new logo for "Lantern Grove Shows" similar in feel to our other brands, Harborlight Market and Tall Cedar Expo. Attached is a graphic showing the three current logos.

Second we are looking for a new overall layout for our holistic living expo program guides that apply this new logo. Each 16-24 page guide has the following sections that need to have templates created that carry out the same look/feel.

a) front and back covers (similar in feel to the Denver Guide attached page 1 or Chicago page 1)
b) Welcome page (similar to the Chicago Guide attached page 3)
c) Expo lecture overview page (similar in feel to the Chicago Guide attached page 7, should only allow for 4 presentation rooms and be vertical to the page.)
d) Left detail page of presentations (similar in feel to the Chicago Guide attached page 34)
e) Right detail page of presentations (similar in feel to the Chicago Guide attached page 35)
f) Detail page for exhibitors (similar in feel to the Chicago Guide attached page 24)
g) Detail page for featured presenters (similar in feel to the Chicago Guide attached page 12)
f) Detail page for secondary featured presenters (similar in feel to the Chicago Guide attached page 15)

Target Market(s)

Casual female 25-54 with interest in holistic subjects

Requirements
Must have
• Logo should have horizontal aspect ratio.

Although samples may be in AI, PSD or PDF, we must have the templates in InDesign native files at the conclusion of the project for all pages of the guide.

Final logo should be vector based.

```html
<!DOCTYPE html>
<html lang="en">
<head>
<meta charset="utf-8">
<title>Workshop Presenters – Lantern Grove Shows</title>
<link href="https://fonts.googleapis.com/css2?family=Arimo:ital,wght@0,400;0,700;1,700&family=Cormorant+Garamond:ital,wght@1,700&display=swap" rel="stylesheet">
<style>
:root{
  --purple:#9b1f8a;
  --navy:#3a3f9a;
  --ink:#1e1e1e;
  --white:#ffffff;
  --backdrop:#e4e4e4;
  --magenta:#a02a92;
}
*{margin:0;padding:0;box-sizing:border-box}
html,body{width:1200px;height:1000px;overflow:hidden}
body{background:var(--backdrop);position:relative;font-family:"Arimo",Arial,sans-serif;color:var(--ink)}
.page{position:absolute;left:266px;top:57px;width:679px;height:873px;background:var(--white)}
.page-header{position:absolute;left:0;top:0;width:679px;height:55px;background:var(--purple)}
.page-header h1{position:absolute;right:27px;top:25px;color:var(--white);font-size:26px;font-weight:700;font-style:italic;letter-spacing:.3px;line-height:28px}
.presenter-name{position:absolute;font-family:"Cormorant Garamond",Georgia,serif;font-style:italic;font-weight:700;font-variant:small-caps;color:var(--navy);font-size:30px;line-height:28px;letter-spacing:.3px}
.photo{position:absolute;width:171px;height:173px;border:5px solid var(--purple)}
.photo .fill{width:100%;height:100%}
.talk{position:absolute}
.talk h2{font-size:19px;font-weight:700;line-height:22px}
.talk .when{font-size:13.5px;line-height:18px;margin-top:4px}
.talk p{font-size:11.8px;line-height:15px;text-align:justify;margin-top:4px}
.talk p + p{margin-top:6px}
.tickets{position:absolute;color:var(--purple);font-size:16px;font-weight:700;line-height:18px}
.included{position:absolute;font-size:10.5px;line-height:12px}
.band{position:absolute;left:0;top:312px;width:679px;height:257px;background:var(--navy);color:var(--white)}
.band .presenter-name{color:var(--white)}
.band .tickets{color:var(--magenta)}
.band .included{color:var(--white)}
.cookbook{position:absolute}
.page-number{position:absolute;left:31px;top:831px;font-size:13px;font-weight:700;color:var(--navy)}
.brand{position:absolute;right:31px;top:830px;font-size:14px;color:var(--navy);font-weight:400;display:flex;align-items:center;gap:6px}
.brand .dot{width:9px;height:9px;border-radius:50%;background:var(--navy)}
</style>
</head>
<body>
<main class="page">
  <header class="page-header"><h1>WORKSHOP PRESENTERS</h1></header>

  <section class="presenter">
    <div class="presenter-name" style="left:30px;top:62px">Marion Vale</div>
    <div class="photo" style="left:29px;top:95px">
      <div class="fill" role="img" aria-label="Portrait photo of presenter Marion Vale" style="background:linear-gradient(160deg,#7d6a55,#c9b59a 55%,#6f8fc4)"></div>
    </div>
    <div class="talk" style="left:214px;top:93px;width:435px">
      <h2>THE POWER TO CHANGE REALITY</h2>
      <div class="when">FRIDAY 4 PM- UTOPIA B (WORKSHOP CENTRAL)</div>
      <p>When we connect to the power of nature, the power of the people in our life, with our own “I Am Presence”, we can manifest anything that we choose. The more connected we grow, the more powerful we become. This workshop gives effective techniques for altering our thoughts and feelings to create luxury, laughter, and love. By exploring false beliefs about our nature and shifting from mind to heart, we can create our best life.</p>
      <p>During the class we will learn the tell-tale signs that we have moved away from our inner knowing. Learn to look for the signs and discover that you have the power to move beyond the limitations that others (and even yourself ) put before you.</p>
    </div>
    <div class="tickets" style="left:30px;top:271px">TICKETS $35</div>
    <div class="included" style="left:30px;top:289px">(or Included with Diamond, Sapphire, Emerald, and Ruby Tickets)</div>
  </section>

  <section class="band">
    <div class="talk" style="left:30px;top:10px;width:437px">
      <h2>THY FOOD BE THY MEDICINE</h2>
      <div class="when">FRIDAY 4 PM- UTOPIA B (WORKSHOP CENTRAL)</div>
      <p>In this workshop, Dr. Calder shares that no one size fits all “diet” or protocol exists. Instead she shows the essential need to find foods that really work for your individual needs. This workshop starts with a self-awareness meditation that facilitates gaining a new sense of yourself. Your brilliant machine of a body has its own unique language. Learn to “heal thyself” by following your signs and symptoms like a health detective.</p>
    </div>
    <div class="talk" style="left:159px;top:149px;width:308px">
      <p>Join Dr. Calder to learn what works to achieve your ideal weight, increase energy, get better sleep, gain a more vibrant mind and lower your risk of disease. Create your own unique optimal health plan today.</p>
    </div>
    <svg class="cookbook" style="left:36px;top:147px" width="100" height="100" viewBox="0 0 100 100" role="img" aria-label="Cookbook cover badge">
      <circle cx="50" cy="50" r="48" fill="#f3ead2" stroke="#c9a96a" stroke-width="3"/>
    </svg>
    <div class="presenter-name" style="right:28px;top:10px">Rina Calder</div>
    <div class="photo" style="left:479px;top:41px;width:171px;height:172px">
      <div class="fill" role="img" aria-label="Photo of presenter Rina Calder holding fruit" style="background:linear-gradient(180deg,#f4f2ef,#e8e4de 50%,#2a2a2a 70%,#141414)"></div>
    </div>
    <div class="tickets" style="right:28px;top:217px">TICKETS $35</div>
    <div class="included" style="right:28px;top:235px">(or Included with Diamond, Sapphire, Emerald, and Ruby Tickets)</div>
  </section>

  <section class="presenter">
    <div class="presenter-name" style="left:30px;top:578px">Janet Orsini-Blake</div>
    <div class="photo" style="left:29px;top:611px">
      <div class="fill" role="img" aria-label="Portrait photo of presenter Janet Orsini-Blake" style="background:linear-gradient(160deg,#8a8a8a,#c98a5a 45%,#a03a22)"></div>
    </div>
    <div class="talk" style="left:214px;top:609px;width:435px">
      <h2>MEET YOUR GUARDIAN ANGELS</h2>
      <div class="when">FRIDAY 4 PM- UTOPIA B (WORKSHOP CENTRAL)</div>
      <p>When we connect to the power of nature, the power of the people in our life, with our own “I Am Presence”, we can manifest anything that we choose. The more connected we grow, the more powerful we become. This workshop gives effective techniques for altering our thoughts and feelings to create luxury, laughter, and love. By exploring false beliefs about our nature and shifting from mind to heart, we can create our best life.</p>
      <p>During the class we will learn the tell-tale signs that we have moved away from our inner knowing. Learn to look for the signs and discover that you have the power to move beyond the limitations that others (and even yourself ) put before you.</p>
    </div>
    <div class="tickets" style="left:30px;top:787px">TICKETS $35</div>
    <div class="included" style="left:30px;top:805px">(or Included with Diamond, Sapphire, Emerald, and Ruby Tickets)</div>
  </section>

  <footer>
    <div class="page-number">page 17</div>
    <div class="brand"><span class="dot"></span>Lantern Grove Shows</div>
  </footer>
</main>
</body>
</html>
```